Square graphic for social media post

I want to create a 1080 x 1080px all-black image for the quote below that I can share on social media. I want the emphasis to be primarily on the quote, secondarily on the portrait, and third (smallest) on the logo. I want the background on the portrait to be edited so it's transparent and just shows the face of the person on a black background (no brick wall visible).

Graphic color: black
Text color: white
Content: "What we went through is going to make the greatest generation of hoteliers our industry has ever seen." << biggest text
Dorian Welk << smaller text
President, Marrowgate Hotels << smaller text
[image of person - use whichever version looks better to you]
[Add Lodging Ledger logo - whichever looks better to you]

This image needs to be readable when sized down much smaller (400x400?) so want the text and portrait to take up most of the space.

I'd like the output both as PNG and original file (preferably Canva). Thanks!

Target Market(s)

Hotel managers

Industry/Entity Type

Hospitality

Font styles to use
Sans Serif

Colors

Designer to choose colors to be used in the design.

Requirements
Must have
• Needs to focus on the quote and the person quoted (the portrait)

```html
<!DOCTYPE html>
<html lang="en">
<head>
<meta charset="utf-8">
<title>Quote Post – Dorian Welk</title>
<link href="https://fonts.googleapis.com/css2?family=Lato:ital,wght@0,400;0,700;0,900;1,700&display=swap" rel="stylesheet">
<style>
  :root {
    --bg: #000000;
    --pattern-a: #1a1a1a;
    --pattern-b: #0e0e0e;
    --text: #ffffff;
    --ring: #ffffff;
    --portrait-light: #ece9e7;
    --portrait-mid: #b9b4c2;
    --portrait-deep: #3d5595;
  }
  * { margin: 0; padding: 0; box-sizing: border-box; }
  html, body {
    width: 1200px;
    height: 1200px;
    overflow: hidden;
    background: var(--bg);
  }
  .post {
    position: relative;
    width: 1200px;
    height: 1200px;
    background: var(--bg);
    overflow: hidden;
    font-family: "Lato", sans-serif;
    color: var(--text);
  }
  .backdrop-pattern {
    position: absolute;
    left: 0;
    top: 0;
    width: 462px;
    height: 1200px;
    background: linear-gradient(180deg, var(--pattern-a) 0%, var(--pattern-b) 55%, var(--pattern-a) 100%);
  }
  .portrait {
    position: absolute;
    left: 0;
    top: 0;
    width: 1200px;
    height: 1200px;
  }
  .quote {
    position: absolute;
    left: 76px;
    top: 108px;
    width: 1110px;
    font-weight: 700;
    font-style: italic;
    font-size: 71px;
    line-height: 83px;
    letter-spacing: -0.5px;
    white-space: nowrap;
  }
  .quote-mark {
    font-weight: 900;
    font-style: normal;
    font-size: 160px;
    line-height: 0;
    position: relative;
  }
  .quote-mark--open { top: 64px; margin-left: -6px; margin-right: 18px; }
  .quote-mark--close { top: 92px; margin-left: 20px; }
  .speaker-name {
    position: absolute;
    left: 80px;
    top: 504px;
    font-weight: 400;
    font-size: 57px;
    letter-spacing: 0.5px;
  }
  .speaker-role {
    position: absolute;
    left: 80px;
    top: 588px;
    font-weight: 400;
    font-size: 40px;
  }
  .speaker-company {
    position: absolute;
    left: 80px;
    top: 640px;
    font-weight: 400;
    font-size: 29px;
  }
  .publisher {
    position: absolute;
    left: 252px;
    top: 940px;
    transform: translateX(-50%);
    display: flex;
    align-items: center;
    gap: 14px;
    white-space: nowrap;
    font-weight: 700;
    font-size: 28px;
    letter-spacing: 6px;
    text-transform: uppercase;
  }
  .publisher-dot {
    width: 12px;
    height: 12px;
    border-radius: 50%;
    background: var(--text);
  }
</style>
</head>
<body>
<main class="post">
  <div class="backdrop-pattern" role="img" aria-label="Faint dark decorative pattern"></div>

  <svg class="portrait" viewBox="0 0 1200 1200" role="img" aria-label="Portrait photo of Dorian Welk in a blue blazer and white shirt, set in a white circle">
    <defs>
      <linearGradient id="portraitFill" x1="0" y1="0" x2="0.6" y2="1">
        <stop offset="0" stop-color="var(--portrait-light)"/>
        <stop offset="0.55" stop-color="var(--portrait-mid)"/>
        <stop offset="1" stop-color="var(--portrait-deep)"/>
      </linearGradient>
    </defs>
    <circle cx="998" cy="1139" r="454" fill="none" stroke="var(--ring)" stroke-width="3"/>
    <circle cx="998" cy="1139" r="392" fill="url(#portraitFill)"/>
  </svg>

  <p class="quote"><span class="quote-mark quote-mark--open">“</span>What we went through is going<br>to make the greatest generation of<br>hoteliers our industry<br>has ever seen<span class="quote-mark quote-mark--close">”</span></p>

  <h1 class="speaker-name">DORIAN WELK</h1>
  <p class="speaker-role">President,</p>
  <p class="speaker-company">Marrowgate Hotels</p>

  <div class="publisher"><span class="publisher-dot"></span>Lodging Ledger</div>
</main>
</body>
</html>
```